KTRA '13 Presentation Dinner

Corvale Junior Hoops Association Inc., or KTRA for short is a local basketball league based in Brisbane Southside, Australia.
We're holding our annual award presentation night and would like to advertise to our 350+ members via posters around the basketball hall and local shopping centres. Majority of our members are in aged 21-30.
The presentation dinner is held at a local Chinese restaurant with lucky door prize, raffles, trivia, '13 highlight video and presentation of '13 awards.
Essential Details are:
Location: Moonvale Restaurant, 4/127 Tallow Rd, Wexburn
Date: Saturday November 23rd 2013
Time: 6:00PM
Dress Code: Formal
See KTRA staff for more details
Optional Detail:
Cost: $400 per table of 10
Discount: Register before 14th September to receive $50 off - $350 per table
The final design should indicate this will be a fun night aimed at young adults and should not be missed by KTRA members.

```html
<!DOCTYPE html>
<html lang="en">
<head>
<meta charset="utf-8">
<title>KTRA '13 Presentation Dinner</title>
<link rel="stylesheet" href="https://fonts.googleapis.com/css2?family=Audiowide&family=PT+Sans+Narrow:wght@400;700&display=swap">
<style>
  :root {
    --backdrop: #c0c0c0;
    --night: #120a1e;
    --league-blue: #1565a8;
    --bar-blue: #175a9c;
    --bar-navy: #272155;
    --bar-maroon: #4a0d2a;
    --bar-magenta: #8c1562;
    --badge-red: #d81b5a;
    --badge-deep: #8a0c38;
    --button: #f6a21e;
    --white: #ffffff;
    --ink: #1d1d3a;
  }
  html, body { margin: 0; padding: 0; width: 1200px; height: 900px; overflow: hidden; }
  body { background: var(--backdrop); position: relative; font-family: "PT Sans Narrow", sans-serif; }

  .poster {
    position: absolute; left: 278px; top: 33px; width: 644px; height: 834px; overflow: hidden;
    background: var(--night);
  }
  .poster-art {
    position: absolute; inset: 0;
    background:
      radial-gradient(circle at 92% 3%, rgba(255,255,255,.95) 0 3%, rgba(255,180,230,.5) 7%, transparent 18%),
      radial-gradient(ellipse at 35% 22%, rgba(214,48,140,.7), transparent 45%),
      radial-gradient(ellipse at 80% 30%, rgba(200,60,170,.55), transparent 40%),
      radial-gradient(ellipse at 50% 45%, rgba(110,50,170,.75), transparent 55%),
      radial-gradient(ellipse at 25% 90%, rgba(30,130,160,.5), transparent 40%),
      linear-gradient(180deg, #2a0f2e 0%, #2a1448 45%, #10182a 80%, #0b1a22 100%);
  }
  .poster-lines {
    position: absolute; inset: 0;
    background: repeating-linear-gradient(135deg, rgba(255,255,255,.05) 0 1px, transparent 1px 6px);
  }

  .headline {
    position: absolute; left: 44px; top: 44px; margin: 0;
    font-family: "Audiowide", sans-serif; font-weight: 400; color: var(--white);
    text-transform: uppercase; font-size: 11px; letter-spacing: 0; line-height: 27px;
    white-space: nowrap;
  }
  .headline .line { display: block; }
  .headline .line-indent { padding-left: 4px; }
  .headline .big { font-size: 17px; }

  .league-mark {
    position: absolute; left: 160px; top: 182px; width: 330px; height: 330px; border-radius: 50%;
    background: var(--league-blue);
    display: flex; align-items: center; justify-content: center;
  }
  .league-name {
    font-family: "PT Sans Narrow", sans-serif; font-weight: 700; font-size: 96px;
    color: var(--white); letter-spacing: 4px;
  }

  .detail {
    position: absolute; left: 0; display: flex; align-items: center; box-sizing: border-box;
    padding-left: 100px; color: var(--white); font-size: 18px; line-height: 21px; white-space: nowrap;
  }
  .detail b { font-weight: 700; }
  .detail-location { top: 560px; height: 50px; width: 334px; background: linear-gradient(90deg, rgba(23,90,156,.55) 0 62px, var(--bar-blue) 62px); }
  .detail-date { top: 613px; height: 33px; width: 362px; background: var(--bar-navy); }
  .detail-time { top: 649px; height: 30px; width: 259px; background: linear-gradient(90deg, rgba(74,13,42,.5) 0 62px, var(--bar-maroon) 62px); }
  .detail-dress { top: 681px; height: 32px; width: 288px; background: linear-gradient(90deg, rgba(140,21,98,.45) 0 62px, var(--bar-magenta) 62px); }

  .more-info {
    position: absolute; left: 186px; top: 732px; width: 188px; height: 35px; border-radius: 5px;
    background: var(--button); color: var(--ink); font-size: 14px;
    display: flex; align-items: center; justify-content: center;
  }

  .price-badge {
    position: absolute; left: 386px; top: 561px; width: 206px; height: 206px; border-radius: 50%;
    background: radial-gradient(circle at 45% 30%, #ff4d86, var(--badge-red) 45%, var(--badge-deep) 100%);
    box-shadow: inset 0 -10px 0 rgba(255,255,255,.18), 0 4px 0 rgba(255,180,210,.45);
    color: var(--white); text-align: center; font-size: 15px;
    display: flex; flex-direction: column; justify-content: center;
  }
  .price-badge p { margin: 0; line-height: 16px; }
  .price-badge p.with-amount { line-height: 22px; }
  .price-badge .amount { font-size: 22px; font-weight: 700; line-height: 1; }
  .price-badge .gap { margin-top: 6px; }
</style>
</head>
<body>
  <main class="poster">
    <div class="poster-art" role="img" aria-label="Night-club style backdrop of a basketball player in pink and violet light with glowing bokeh circles"></div>
    <div class="poster-lines"></div>

    <h1 class="headline">
      <span class="line">The presentation dinner is held at a local</span>
      <span class="line">Chinese restaurant with <span class="big">Lucky door prize,</span></span>
      <span class="line line-indent">Raffles, trivia, '13 highlight video and presentation of <span class="big">'13 Awards.</span></span>
    </h1>

    <div class="league-mark">
      <span class="league-name">KTRA</span>
    </div>

    <div class="detail detail-location"><span>Location: <b>Moonvale Restaurant,<br>4/127 Tallow Rd, Wexburn</b></span></div>
    <div class="detail detail-date"><span>Date: <b>Saturday November 23rd 2013</b></span></div>
    <div class="detail detail-time"><span>Time: <b>6:00PM</b></span></div>
    <div class="detail detail-dress"><span>Dress Code: <b>Formal</b></span></div>

    <div class="more-info">See KTRA staff for more details</div>

    <div class="price-badge">
      <p>Cost:</p>
      <p class="with-amount"><span class="amount">$400</span> per table of 10</p>
      <p class="gap">Discount:</p>
      <p>Register before</p>
      <p>14th September</p>
      <p class="with-amount">to receive <span class="amount">$50</span> off -</p>
      <p class="with-amount"><span class="amount">$350</span> per table</p>
    </div>
  </main>
</body>
</html>
```